RT Website Home Page Design

The task is to develop a winning design for a replacement website for our client RT Plumbing, Heating, AC & Remodeling. ct

```html
<!DOCTYPE html>
<html lang="en">
<head>
<meta charset="utf-8">
<title>RT Plumbing, Heating, AC &amp; Remodeling – Home</title>
<link rel="stylesheet" href="https://fonts.googleapis.com/css2?family=Fira+Sans:wght@400;500;600;700&family=Lato:wght@400;700&display=swap">
<style>
:root{
  --navy:#1d2b4f;
  --blue:#0a4fa8;
  --ink:#1a1a1a;
  --text:#333;
  --muted:#f1f1f1;
  --soft:#f7f7f7;
  --yellow:#f4e04d;
  --white:#fff;
  --line:#c9c9c9;
}
*{box-sizing:border-box;margin:0;padding:0}
html,body{width:1200px;height:4886px;overflow:hidden}
body{position:relative;background:var(--white);font-family:"Lato",sans-serif;color:var(--text)}
.abs{position:absolute}
h1,h2,h3,.heading{font-family:"Fira Sans",sans-serif}
.pill{display:inline-flex;align-items:center;justify-content:center;background:var(--navy);color:var(--white);border-radius:30px;font-family:"Fira Sans",sans-serif;font-weight:500;text-decoration:none}

/* header */
.site-header{top:0;left:0;width:1200px;height:115px;background:var(--white)}
.brand{display:flex;align-items:center;gap:10px;font-family:"Fira Sans",sans-serif;font-weight:700;color:var(--navy);text-transform:uppercase;line-height:1.15}
.brand .mark{width:22px;height:22px;border-radius:50%;background:var(--blue);flex:none}
.header-brand{left:115px;top:28px;font-size:17px;width:220px}
.service-area{left:356px;top:22px;font-family:"Fira Sans",sans-serif;font-weight:500;font-size:17px;color:var(--ink);line-height:1.5}
.header-btn{top:25px;height:32px;width:142px;font-size:11px}
.header-phone{top:64px;font-family:"Fira Sans",sans-serif;font-weight:500;font-size:16px;color:var(--navy);width:142px;text-align:center}
.main-nav{top:115px;left:0;width:1200px;height:57px;background:var(--navy);display:flex;align-items:center;gap:27px;padding-left:100px}
.main-nav a{color:var(--white);font-family:"Fira Sans",sans-serif;font-size:13px;text-decoration:none}

/* hero */
.hero{top:172px;left:0;width:1200px;height:493px;background:linear-gradient(180deg,#3f78b9 0%,#8fb6d8 45%,#b9c6c7 62%,#6f8748 78%,#4b6a2d 100%)}
.hero h1{position:absolute;left:107px;top:100px;font-size:40px;line-height:56px;font-weight:700;color:var(--white)}
.hero h1 span{color:var(--navy)}
.hero .pill{position:absolute;left:103px;top:235px;width:302px;height:57px;background:var(--blue);font-size:19px}

/* services */
.section-title{width:1200px;left:0;text-align:center;font-weight:700;font-size:34px;color:var(--ink)}
.service-card{width:236px;height:240px;background:var(--blue);border-radius:4px;color:var(--white);padding:22px 16px}
.service-card svg{display:block;margin-bottom:26px}
.service-card h3{font-size:20px;font-weight:600;margin-bottom:16px;line-height:1.45}
.service-card p{font-size:14px;line-height:1.7}

/* request */
.request-panel{left:0;top:1420px;width:632px;height:578px;background:var(--muted)}
.request-photo{left:567px;top:1396px;width:633px;height:531px;background:linear-gradient(160deg,#2f5d66 0%,#2a6a74 40%,#b28a66 70%,#d8d1c6 100%)}
.request-panel h2{position:absolute;left:99px;top:28px;font-size:32px;font-weight:600;color:var(--ink)}
.field{position:absolute;left:99px;width:468px;height:48px;background:var(--white);border:1px solid var(--line);border-radius:12px;padding:0 16px;line-height:46px;font-size:14px;color:#444}
.field.comments{height:122px;line-height:1;padding-top:14px;left:104px;width:460px}
.request-panel .pill{position:absolute;left:105px;top:491px;width:147px;height:46px;font-size:15px}

/* reminder */
.reminder h2{position:absolute;left:99px;top:2095px;font-size:34px;font-weight:600;color:var(--ink)}
.reminder p{position:absolute;left:99px;top:2155px;width:352px;font-size:15px;line-height:32px;color:var(--ink)}
.reminder .pill{position:absolute;left:101px;top:2372px;width:147px;height:46px;font-size:16px}
.reminder-photo{left:590px;top:2078px;width:512px;height:360px;background:linear-gradient(135deg,#a9a496 0%,#d4cfc4 45%,#8c8578 100%)}

/* difference */
.difference{top:2478px;left:0;width:1200px;height:757px;background:linear-gradient(180deg,#f7f7f5 0%,#f0efec 55%,#e1c46a 70%,#b9ad9f 82%,#9e9288 100%)}
.difference h2{position:absolute;width:1200px;text-align:center;top:35px;font-size:34px;font-weight:600;color:var(--ink)}
.difference p{position:absolute;left:150px;width:900px;top:105px;text-align:center;font-size:16px;line-height:32px;color:var(--ink);font-weight:700}
.difference .pill{position:absolute;left:528px;top:267px;width:145px;height:45px;font-size:15px}

/* savings */
.offer{width:304px;height:304px;border-radius:50%;background:var(--blue);overflow:hidden;text-align:center;color:var(--white)}
.offer h3{font-size:25px;font-weight:500;line-height:33px;padding-top:22px}
.offer p{font-size:20px;line-height:33px;margin-top:12px}
.offer .save{position:absolute;left:0;bottom:0;width:304px;height:96px;background:var(--yellow);color:var(--ink);font-family:"Fira Sans",sans-serif;font-weight:700;font-size:34px;line-height:68px;padding-bottom:28px}
.offer .single{padding-top:55px}

/* blog */
.blog{top:3852px;left:0;width:1200px;height:568px;background:var(--soft)}
.blog-card{top:133px;width:322px;height:375px;background:var(--white);box-shadow:0 3px 10px rgba(0,0,0,.12);padding:8px}
.blog-card .thumb{height:205px;border-radius:10px;position:relative}
.blog-card .date{position:absolute;left:14px;bottom:12px;display:flex;align-items:center;gap:10px;color:var(--white);font-size:13px}
.blog-card .date i{width:32px;height:32px;border-radius:50%;background:var(--blue);display:inline-flex;align-items:center;justify-content:center}
.blog-card h3{font-size:19px;font-weight:500;color:var(--ink);margin:14px 4px 10px;line-height:26px;height:52px}
.blog-card p{font-size:14px;line-height:24px;color:#333;margin:0 4px;height:52px}
.blog-card a{display:block;margin:16px 4px 0;color:var(--blue);font-weight:700;font-size:14px;text-decoration:none}

/* footer */
.footer-brand{left:125px;top:4495px;font-size:24px;width:250px}
.footer-about{left:99px;top:4630px;width:310px;font-size:13px;line-height:24px;color:var(--ink)}
.social{left:107px;top:4700px;width:26px;height:26px;background:var(--ink);border-radius:3px}
.footer-col h4{font-family:"Fira Sans",sans-serif;font-weight:500;font-size:24px;color:var(--ink)}
.footer-links a{display:block;font-size:14px;color:var(--ink);text-decoration:none;margin-bottom:19px}
.contact-line{display:flex;align-items:flex-start;gap:14px;font-size:16px;color:var(--ink);line-height:30px}
.pay-card{width:78px;height:46px;border:1px solid #ddd;background:#eef1f6;border-radius:4px}
.copyright{top:4812px;width:1200px;left:0;text-align:center;font-size:16px;color:var(--ink)}
</style>
</head>
<body>

<header class="abs site-header">
  <div class="abs brand header-brand"><span class="mark"></span><span>RT Plumbing<br><small style="font-size:10px">Heating, AC &amp; Remodeling</small></span></div>
  <div class="abs service-area">Serving Maple Ridge, MA &amp;<br>Neighboring Communities</div>
  <a class="abs pill header-btn" style="left:680px">Request Service</a>
  <a class="abs pill header-btn" style="left:834px">Request a Quote</a>
  <div class="abs header-phone" style="left:680px">508.555.0142</div>
  <div class="abs header-phone" style="left:834px">800.555.0187</div>
</header>

<nav class="abs main-nav">
  <a>About</a><a>Plumbing</a><a>Water Heaters</a><a>Heating</a><a>Air Conditioning</a><a>Indoor Air Quality</a><a>Commercial</a><a>Handy Work &amp; Remodeling</a><a>Contact</a>
</nav>

<section class="abs hero" role="img" aria-label="Blue-roofed house on a green lawn under a sunny sky">
  <h1>Enjoy the <span>Best of Home Living</span><br>Indoors &amp; Out.</h1>
  <a class="pill">Contact Us to Get Started</a>
</section>

<h2 class="abs section-title" style="top:735px">More of What You Need</h2>
<div class="abs service-card" style="left:99px;top:808px"><svg width="54" height="54" viewBox="0 0 54 54" fill="none" stroke="#fff" stroke-width="2.5"><path d="M8 48V14h14v18h10V6h14v42"/></svg><h3>Plumbing</h3><p>Lorem ipsum dolor sit amet, consectetur adipiscing elit, sed do eiusmod</p></div>
<div class="abs service-card" style="left:355px;top:808px"><svg width="54" height="54" viewBox="0 0 54 54" fill="none" stroke="#fff" stroke-width="2.5"><rect x="12" y="4" width="30" height="42" rx="4"/><circle cx="27" cy="18" r="6"/><path d="M18 50h18"/></svg><h3>Water Heaters</h3><p>Lorem ipsum dolor sit amet, consectetur adipiscing elit, sed do eiusmod</p></div>
<div class="abs service-card" style="left:611px;top:808px"><svg width="54" height="54" viewBox="0 0 54 54" fill="none" stroke="#fff" stroke-width="2.5"><rect x="6" y="20" width="42" height="26" rx="3"/><path d="M14 20v26M22 20v26M30 20v26M38 20v26M16 6v8M27 6v8M38 6v8"/></svg><h3>Heating</h3><p>Lorem ipsum dolor sit amet, consectetur adipiscing elit, sed do eiusmod</p></div>
<div class="abs service-card" style="left:866px;top:808px"><svg width="54" height="54" viewBox="0 0 54 54" fill="none" stroke="#fff" stroke-width="2.5"><rect x="4" y="6" width="46" height="18" rx="3"/><circle cx="18" cy="38" r="9"/><path d="M34 32v14M42 32v14"/></svg><h3>Air Conditioning</h3><p>Lorem ipsum dolor sit amet, consectetur adipiscing elit, sed do eiusmod</p></div>

<div class="abs service-card" style="left:99px;top:1086px"><svg width="54" height="54" viewBox="0 0 54 54" fill="none" stroke="#fff" stroke-width="2.5"><path d="M6 18h30a7 7 0 1 0-7-7M6 28h40a7 7 0 1 1-7 7M6 38h18"/></svg><h3>Indoor Air Quality</h3><p>Lorem ipsum dolor sit amet, consectetur adipiscing elit, sed do eiusmod</p></div>
<div class="abs service-card" style="left:355px;top:1086px"><svg width="54" height="54" viewBox="0 0 54 54" fill="none" stroke="#fff" stroke-width="2.5"><rect x="8" y="16" width="14" height="32" rx="3"/><rect x="32" y="16" width="14" height="32" rx="3"/><path d="M8 10h38M22 26h10"/></svg><h3>Water Filtration</h3><p>Lorem ipsum dolor sit amet, consectetur adipiscing elit, sed do eiusmod</p></div>
<div class="abs service-card" style="left:611px;top:1086px"><svg width="54" height="54" viewBox="0 0 54 54" fill="none" stroke="#fff" stroke-width="2.5"><rect x="6" y="8" width="42" height="34" rx="2"/><path d="M18 30l9-10 9 10M4 48h46"/></svg><h3>Remodeling &amp; Handy Work</h3><p>Lorem ipsum dolor sit amet, consectetur adipiscing elit,</p></div>
<div class="abs service-card" style="left:866px;top:1086px"><svg width="54" height="54" viewBox="0 0 54 54" fill="none" stroke="#fff" stroke-width="2.5"><rect x="6" y="12" width="42" height="34" rx="2"/><path d="M27 20c6 7 6 12 0 18c-6-6-6-11 0-18z"/></svg><h3>Gas Fireplaces</h3><p>Lorem ipsum dolor sit amet, consectetur adipiscing elit, sed do eiusmod</p></div>

<div class="abs request-photo" role="img" aria-label="Modern kitchen with teal wall, hanging plant and wooden bar stools"></div>
<section class="abs request-panel">
  <h2>Request Service</h2>
  <div class="field" style="top:88px">Name</div>
  <div class="field" style="top:152px">Phone</div>
  <div class="field" style="top:216px">Address</div>
  <div class="field" style="top:278px">Email</div>
  <div class="field comments" style="top:344px">Comments</div>
  <a class="pill">SUBMIT NOW</a>
</section>

<section class="reminder">
  <h2>Back to School Reminder</h2>
  <p>Most families see an uptick in morning “rush hour” activity once the school year begins, and so does your water heater. Can yours keep up with the increased demand? Contact us today for a water heater check-up and free quote on a replacement system.</p>
  <a class="pill">Read More</a>
  <div class="abs reminder-photo" role="img" aria-label="Bathroom with tiled shower and glass door"></div>
</section>

<section class="abs difference" role="img" aria-label="Smiling woman relaxing with arms outstretched on a sofa beside a plant">
  <h2>The RT Difference Makers</h2>
  <p>RT is a favorite choice among homeowners who appreciate our extensive range of home comfort and related services. Others like us best for our 100% satisfaction guarantee, while still others enjoy the many benefits that membership in our Preferred Service Club provides. Add it all up, and there’s a lot to like about RT Plumbing, Heating, AC &amp; Remodeling.</p>
  <a class="pill">Learn More</a>
</section>

<h2 class="abs section-title" style="top:3300px">Enjoy the Savings...Plus the Added Comfort!</h2>
<div class="abs offer" style="left:123px;top:3400px"><h3>New<br>Water Heater</h3><p>on a new water heater,<br>tank-style or tankless.</p><div class="save">Save $120</div></div>
<div class="abs offer" style="left:451px;top:3400px"><h3 class="single">HVAC System</h3><p>on a new heating or<br>cooling system.</p><div class="save">Save $350</div></div>
<div class="abs offer" style="left:780px;top:3400px"><h3>First-time<br>Customer</h3><p>on any service we<br>provide</p><div class="save">Save $35</div></div>
<a class="abs pill" style="left:528px;top:3752px;width:145px;height:46px;font-size:15px">View all</a>

<section class="abs blog">
  <h2 class="abs section-title" style="top:38px">Latest Blog Feeds</h2>
  <article class="abs blog-card" style="left:97px">
    <div class="thumb" role="img" aria-label="House with patio furniture on a wooden deck" style="background:linear-gradient(160deg,#9dbc6a,#b59b76 60%,#6f5a42)"><span class="date"><i><svg width="14" height="14" viewBox="0 0 14 14" fill="#fff"><rect x="1" y="3" width="12" height="10" rx="1"/></svg></i>30 MAY 2023</span></div>
    <h3>The Benefits of an AC Tune-Up</h3><p>How do you prepare your home for spring and summer?</p><a>READ MORE &nbsp;»</a>
  </article>
  <article class="abs blog-card" style="left:437px">
    <div class="thumb" role="img" aria-label="Bright bathroom with walk-in shower" style="background:linear-gradient(160deg,#d9d6d0,#a8a39b 60%,#7b766f)"><span class="date"><i><svg width="14" height="14" viewBox="0 0 14 14" fill="#fff"><rect x="1" y="3" width="12" height="10" rx="1"/></svg></i>30 MAY 2023</span></div>
    <h3>How to Choose the Best Toilet Style</h3><p>It may seem like such a simple</p><a>READ MORE &nbsp;»</a>
  </article>
  <article class="abs blog-card" style="left:776px">
    <div class="thumb" role="img" aria-label="Family relaxing on a sofa under a wall-mounted air conditioner" style="background:linear-gradient(160deg,#e4e1dc,#c3bbb0 60%,#8d8479)"><span class="date"><i><svg width="14" height="14" viewBox="0 0 14 14" fill="#fff"><rect x="1" y="3" width="12" height="10" rx="1"/></svg></i>30 MAY 2023</span></div>
    <h3>Beat the Summer Heat with Ductless Air</h3><p>For decades, central air conditioning</p><a>READ MORE &nbsp;»</a>
  </article>
</section>

<footer>
  <div class="abs brand footer-brand"><span class="mark"></span><span>RT Plumbing<br><small style="font-size:13px">Heating, AC &amp; Remodeling</small></span></div>
  <p class="abs footer-about">"Lorem ipsum dolor sit amet, consectetur adipiscing elit, sed do eiusmod tempor incididunt ut labore et dolore magna aliqua.</p>
  <div class="abs social" aria-label="Social link"></div>

  <div class="abs footer-col" style="left:413px;top:4474px"><h4>MENU</h4></div>
  <nav class="abs footer-links" style="left:415px;top:4530px"><a>About</a><a>Plumbing</a><a>Water Heaters</a><a>Heating</a><a>Air Conditioning</a></nav>
  <nav class="abs footer-links" style="left:593px;top:4530px"><a>Indoor Air Quality</a><a>Commercial</a><a>Handy Work &amp; Remodeling</a><a>Contact</a></nav>

  <div class="abs footer-col" style="left:845px;top:4476px"><h4>CONTACT US</h4></div>
  <div class="abs" style="left:835px;top:4526px">
    <div class="contact-line"><svg width="14" height="20" viewBox="0 0 14 20" style="margin-top:6px"><path d="M7 0a7 7 0 0 0-7 7c0 5 7 13 7 13s7-8 7-13a7 7 0 0 0-7-7z" fill="#1a1a1a"/><circle cx="7" cy="7" r="2.5" fill="#fff"/></svg><span>18 Linden Court<br>Milford, MA 01757</span></div>
    <div class="contact-line" style="margin-top:14px"><svg width="16" height="16" viewBox="0 0 24 24" style="margin-top:7px"><path d="M6.6 10.8a15 15 0 0 0 6.6 6.6l2.2-2.2c.3-.3.7-.4 1-.2 1.1.4 2.3.6 3.6.6.6 0 1 .4 1 1V20c0 .6-.4 1-1 1A17 17 0 0 1 3 4c0-.6.4-1 1-1h3.5c.6 0 1 .4 1 1 0 1.3.2 2.5.6 3.6.1.3 0 .7-.2 1z" fill="#1a1a1a"/></svg><span>+1 508.555.0142</span></div>
    <div class="contact-line" style="margin-top:14px"><svg width="18" height="14" viewBox="0 0 18 14" style="margin-top:9px"><rect x="1" y="1" width="16" height="12" fill="none" stroke="#1a1a1a" stroke-width="1.6"/><path d="M1 1l8 7 8-7" fill="none" stroke="#1a1a1a" stroke-width="1.6"/></svg><span>info@rtheatingplumbing.com</span></div>
  </div>
  <div class="abs" style="left:583px;top:4716px;display:flex;gap:9px" aria-label="Accepted payment methods">
    <div class="pay-card"></div><div class="pay-card"></div><div class="pay-card"></div><div class="pay-card"></div><div class="pay-card"></div><div class="pay-card"></div>
  </div>
  <p class="abs copyright">Copyright ©2023 &nbsp;RTheatingplumbing. All Rights Reserved</p>
</footer>

</body>
</html>
```